Microlight Aircraft Website Project

Need a website designed, or at least a template made, that my web programmer can work with here. We are a new manufacturer of microlight aircraft & powered hang gliders. Our company name is Brisk Fern. We manufacture portable utility aircraft in the Light Sport category (formerly known as Ultralights or Microlights). Our particular design is a 2-seat powered hang glider and caters to those who want to go explore the backcountry. We are not necessarily aviation nuts, but more into the development of a flying utility vehicle for extreme exploration and expeditions. We have been importing these aircraft from 3 countries for 15 years and have supplied over 200 expedition-quality aircraft world-wide. We are now manufacturing here in the US.

Industry/Entity Type

Manufacturer

Coding

Coded - Design and coding required

```html
<!DOCTYPE html>
<html lang="en">
<head>
<meta charset="utf-8">
<title>Brisk Fern — Micro Light Aircraft &amp; Powered Hang Gliders</title>
<link href="https://fonts.googleapis.com/css2?family=Lato:wght@400;700&family=Questrial&display=swap" rel="stylesheet">
<style>
:root{
  --navy:#0d1f56;
  --royal:#2d3f8f;
  --accent:#3a53b0;
  --sky:#4b68b6;
  --deep:#2b2f78;
  --pale:#eceef5;
  --ink:#1c1c1c;
  --muted:#555;
  --white:#fff;
  --dark:#1e1e22;
}
*{box-sizing:border-box;margin:0;padding:0}
html,body{width:821px;height:1200px;overflow:hidden}
body{position:relative;font-family:"Lato",sans-serif;color:var(--ink);background:var(--white)}
.abs{position:absolute}
.heading{font-family:"Questrial",sans-serif;font-weight:400}

/* header */
.topline{left:0;top:0;width:600px;height:2px;background:var(--accent)}
.topline.dark{left:600px;width:221px;background:#222}
.brand{left:110px;top:24px;display:flex;align-items:center;gap:8px}
.brand-dot{width:22px;height:22px;background:var(--navy);border-radius:50%}
.brand-name{font-family:"Lato",sans-serif;font-weight:700;font-size:22px;color:var(--navy);letter-spacing:1px}
.social{display:flex;gap:8px}
.social span{width:24px;height:24px;border:1.5px solid var(--navy);border-radius:50%;display:block}
.header-social{left:597px;top:10px}
.contact-row{top:45px;display:flex;align-items:center;gap:6px;font-size:10px;font-weight:700;color:var(--navy)}
.contact-icon{width:22px;height:22px;border:1.5px solid var(--navy);border-radius:50%;display:flex;align-items:center;justify-content:center}

/* nav */
.nav{left:0;top:80px;width:821px;height:26px;background:var(--navy);display:flex;padding-left:88px}
.nav a{color:var(--white);text-decoration:none;font-size:11px;height:26px;line-height:27px;padding:0 23px;border-right:1px solid #2c3d78}
.nav a:last-child{border-right:0}
.nav a.active{background:var(--pale);color:var(--navy);border-right:0}

/* hero */
.hero{left:0;top:106px;width:821px;height:282px;background:linear-gradient(180deg,#3d5a6e 0%,#2f4f62 45%,#1f3b4e 100%)}
.hero-title{right:112px;top:66px;text-align:right;color:var(--white);font-size:20px;line-height:27px;text-shadow:0 1px 3px rgba(0,0,0,.5)}
.hero-arrow{top:126px;width:30px;height:30px;border-radius:50%;border:1px solid rgba(255,255,255,.4);background:rgba(255,255,255,.12);display:flex;align-items:center;justify-content:center}

/* about */
.about{left:0;top:388px;width:821px;height:152px;background:var(--pale)}
.about-label{left:111px;top:46px;font-size:21px;color:var(--ink)}
.about-title{left:111px;top:72px;font-size:31px;color:var(--royal)}
.about-rule{left:283px;top:28px;width:2px;height:96px;background:linear-gradient(var(--accent),var(--navy))}
.about-text{left:325px;top:33px;width:386px;font-size:7.6px;line-height:14.7px;color:#333}
.about-text a{color:var(--accent)}

/* service panels */
.panel{top:540px;width:411px;height:282px;text-align:center;color:var(--white)}
.panel.micro{left:0;background:linear-gradient(160deg,#2d3a7e,#25306a)}
.panel.glider{left:410px;background:linear-gradient(160deg,#4a66b4,#3c57a8)}
.panel-icon{display:block;margin:44px auto 0;width:120px;height:46px}
.panel h2{font-size:22px;margin-top:14px;letter-spacing:.3px}
.panel p{font-size:9px;line-height:13px;width:220px;margin:10px auto 0}
.btn{display:inline-block;margin-top:20px;width:101px;height:26px;line-height:26px;background:var(--white);color:var(--royal);font-size:10px;font-weight:700;border-radius:2px}

/* news + gallery */
.section-head{top:853px;width:278px;border-bottom:1px solid #222;padding-bottom:2px;font-size:19px}
.section-head em{font-style:normal;color:var(--accent)}
.pager{top:857px;display:flex;gap:3px}
.pager span{width:10px;height:10px;border:1px solid #888;border-radius:50%}
.news-item{left:110px;width:268px;display:flex;gap:13px}
.date{width:33px;flex:none;text-align:center;color:var(--white)}
.date b{display:block;height:22px;background:var(--accent);font-size:16px;line-height:22px}
.date i{display:block;height:13px;background:var(--navy);font-style:normal;font-size:7px;line-height:13px}
.news-item h3{font-size:8.5px;font-weight:700;margin-top:-2px}
.news-item p{font-size:7.8px;line-height:11px;margin-top:3px;color:#333}
.news-item a{font-size:7px;color:var(--accent);font-weight:700;text-decoration:none}
.divider{left:110px;width:268px;height:1px;background:#ddd}
.thumb{top:889px;width:88px;height:88px}
.view-all{left:432px;top:993px;font-size:7.5px;color:var(--accent);font-weight:700}

/* footer */
.footer{left:0;top:1032px;width:821px;height:140px;background:linear-gradient(180deg,#2d2c7c,#26287a);color:var(--white)}
.footer h4{font-size:12px;font-weight:400;border-bottom:1px solid rgba(255,255,255,.2);padding-bottom:3px}
.links{display:grid;grid-template-columns:70px 60px;row-gap:8px;margin-top:6px;font-size:8.5px}
.links span::before{content:"› ";}
.vrule{top:22px;width:1px;height:108px;background:rgba(255,255,255,.2)}
.info-line{display:flex;gap:8px;font-size:8px;line-height:11px;margin-top:10px}
.map{left:456px;top:25px;width:128px;height:93px;background:linear-gradient(135deg,#e8e4da,#d8d6cc);border:2px solid var(--white)}
.footer-brand{left:622px;top:52px;font-weight:700;font-size:12px;letter-spacing:1px;color:#b9bde0}
.footer-social{left:617px;top:87px}
.footer-social span{border-color:var(--white);background:rgba(255,255,255,.15)}
.copyright{left:0;top:1172px;width:821px;height:28px;background:var(--dark);color:#ccc;font-size:8px;text-align:center;line-height:28px}
</style>
</head>
<body>

<header>
  <div class="abs topline"></div>
  <div class="abs topline dark"></div>
  <div class="abs brand"><span class="brand-dot"></span><span class="brand-name">BRISK FERN</span></div>
  <div class="abs social header-social" aria-label="Social links"><span></span><span></span><span></span><span></span></div>
  <div class="abs contact-row" style="left:494px">
    <span class="contact-icon"><svg width="11" height="11" viewBox="0 0 24 24"><path fill="#0d1f56" d="M6.6 10.8a15 15 0 006.6 6.6l2.2-2.2c.3-.3.7-.4 1-.2 1.1.4 2.3.6 3.6.6.6 0 1 .4 1 1V20c0 .6-.4 1-1 1A17 17 0 013 4c0-.6.4-1 1-1h3.5c.6 0 1 .4 1 1 0 1.3.2 2.5.6 3.6.1.3 0 .7-.2 1z"/></svg></span>
    020 - 555 - 0148
  </div>
  <div class="abs contact-row" style="left:604px">
    <span class="contact-icon"><svg width="11" height="9" viewBox="0 0 24 18"><path fill="#0d1f56" d="M0 0h24v18H0z"/><path d="M1 1l11 9 11-9" stroke="#fff" stroke-width="2" fill="none"/></svg></span>
    hello@briskfern.com
  </div>
</header>

<nav class="abs nav">
  <a class="active">Home</a><a>Company</a><a>Ready to Fly</a><a>Gallery</a><a>Training</a><a>Downloads</a><a>Contact Us</a>
</nav>

<section class="abs hero" role="img" aria-label="Photo of a hang glider pilot soaring above misty mountain valleys">
  <h1 class="abs heading hero-title">We Are Manufacturer of<br>Micro Light Aircraft &amp;<br>Powered Hang Gliders</h1>
  <div class="abs hero-arrow" style="left:17px"><svg width="10" height="16"><path d="M8 1L2 8l6 7" stroke="#fff" fill="none" stroke-width="1.5"/></svg></div>
  <div class="abs hero-arrow" style="left:774px"><svg width="10" height="16"><path d="M2 1l6 7-6 7" stroke="#fff" fill="none" stroke-width="1.5"/></svg></div>
</section>

<section class="abs about">
  <div class="abs heading about-label">About</div>
  <div class="abs heading about-title">BRISK FERN</div>
  <div class="abs about-rule"></div>
  <p class="abs about-text">Lorem ipsum dolor sit amet, consectetuer adipiscing elit, sed diam nonummy nibh euismod tincidunt ut laoreet dolore magna aliquam erat volutpat. Ut wisi enim ad minim veniam, quis nostrud exerci tation ullamcorper suscipit lobortis nisl ut aliquip ex ea commodo consequat. Duis autem vel eum iriure dolor in hendrerit in vulputate velit esse molestie consequat, vel illum dolore eu feugiat nulla facilisis at vero eros et accumsan et iusto odio dignissim qui blandit praesent luptatum zzril delenit augue duis dolore te feugait nulla facilisi. Exerci tation ullamcorper suscipit lobortis nisl ut aliquip ex ea commodo consequat <a>More</a> <a>[+]</a></p>
</section>

<section class="abs panel micro">
  <svg class="panel-icon" role="img" aria-label="Micro light aircraft illustration" viewBox="0 0 120 46"><rect x="10" y="8" width="100" height="30" rx="15" fill="rgba(255,255,255,.12)"/></svg>
  <h2 class="heading">Micro Light Aircraft</h2>
  <p>Lorem ipsum dolor sit amet, consectetuer adipiscing elit, sed diam nonummy nibh euismod tincidunt ut laoreet dolore magna aliquam erat volutpat. Ut wisi enim ad minim veniam.</p>
  <span class="btn">Read More</span>
</section>
<section class="abs panel glider">
  <svg class="panel-icon" role="img" aria-label="Powered hang glider illustration" viewBox="0 0 120 46"><rect x="10" y="8" width="100" height="30" rx="15" fill="rgba(255,255,255,.14)"/></svg>
  <h2 class="heading">Powered Hang Gliders</h2>
  <p>Lorem ipsum dolor sit amet, consectetuer adipiscing elit, sed diam nonummy nibh euismod tincidunt ut laoreet dolore magna aliquam erat volutpat. Ut wisi enim ad minim veniam.</p>
  <span class="btn">Read More</span>
</section>

<section>
  <h2 class="abs heading section-head" style="left:110px">Latest <em>News</em></h2>
  <div class="abs pager" style="left:364px"><span></span><span></span></div>
  <article class="abs news-item" style="top:888px">
    <div class="date"><b>30</b><i>APR</i></div>
    <div><h3>Duis autem vel eum iriure dolor in hendrerit molestie</h3>
    <p>Lorem ipsum dolor sit amet, consectetuer adipiscing elit, sed diam nonummy nibh euismod tincidunt ut laoreet</p><a>Read More »</a></div>
  </article>
  <div class="abs divider" style="top:944px"></div>
  <article class="abs news-item" style="top:954px">
    <div class="date"><b>31</b><i>APR</i></div>
    <div><h3>Allamcorper suscipit lobortis col hendrerit in vulputate</h3>
    <p>Lorem ipsum dolor sit amet, consectetuer adipiscing elit, sed diam nonummy nibh euismod tinci</p><a>Read More »</a></div>
  </article>

  <h2 class="abs heading section-head" style="left:432px">Photo <em>Gallery</em></h2>
  <div class="abs pager" style="left:687px"><span></span><span></span></div>
  <div class="abs thumb" style="left:432px;background:linear-gradient(#4a7fc8,#b45a2c)" role="img" aria-label="Photo of a microlight flying over red canyons"></div>
  <div class="abs thumb" style="left:527px;background:linear-gradient(#6a8a4a,#8a9a6a)" role="img" aria-label="Photo of a microlight above green fields"></div>
  <div class="abs thumb" style="left:622px;background:linear-gradient(#3b5ec0,#d9e0ee)" role="img" aria-label="Photo of a colourful hang glider over snowy mountains"></div>
  <a class="abs view-all">View All »</a>
</section>

<footer class="abs footer">
  <div class="abs" style="left:110px;top:22px;width:128px">
    <h4 class="heading">Quick Links</h4>
    <div class="links"><span>Home</span><span>Training</span><span>Company</span><span>Downloads</span><span>Ready to Fly</span><span>Contact Us</span><span>Gallery</span></div>
  </div>
  <div class="abs vrule" style="left:252px"></div>
  <div class="abs" style="left:271px;top:22px;width:153px">
    <h4 class="heading">Contact Information</h4>
    <div class="info-line"><svg width="7" height="10" viewBox="0 0 10 14"><path fill="#fff" d="M5 0a5 5 0 00-5 5c0 4 5 9 5 9s5-5 5-9a5 5 0 00-5-5zm0 7a2 2 0 110-4 2 2 0 010 4z"/></svg><span>Lorem ipsum dolor sit amet consec tetuer adipiscing elit - 12345.</span></div>
    <div class="info-line" style="margin-top:12px"><svg width="8" height="8" viewBox="0 0 24 24"><path fill="#fff" d="M6.6 10.8a15 15 0 006.6 6.6l2.2-2.2c.3-.3.7-.4 1-.2 1.1.4 2.3.6 3.6.6.6 0 1 .4 1 1V20c0 .6-.4 1-1 1A17 17 0 013 4c0-.6.4-1 1-1h3.5c.6 0 1 .4 1 1 0 1.3.2 2.5.6 3.6.1.3 0 .7-.2 1z"/></svg><span>(555) 204 - 3311</span></div>
    <div class="info-line" style="margin-top:12px"><svg width="8" height="6" viewBox="0 0 24 18"><path fill="#fff" d="M0 0h24v18H0z"/></svg><span>hello@briskfern.com</span></div>
  </div>
  <div class="abs vrule" style="left:438px"></div>
  <div class="abs map" role="img" aria-label="Street map showing the office location"></div>
  <div class="abs vrule" style="left:598px"></div>
  <div class="abs footer-brand">BRISK FERN</div>
  <div class="abs social footer-social" aria-label="Social links"><span></span><span></span><span></span><span></span></div>
</footer>
<div class="abs copyright">Copyright 2016 © BRISK FERN. All rights reserved.</div>

</body>
</html>
```